BANNER PUBBLICITARIO FACEBOOK

Advertise our services via facebook.
We are a medical center of diagnostic imaging, perform MRI, CT, ultrasound and specialist visits. I want to advertise our center through Facebook trying to get the knowledge of our center to as many people as possible. our target audience are people from 18 to 80 years old.
I want to highlight our contact details, our address and our website www. corvalux.it. All contact information can be found on our website

Target Market(s)

my target market are people from 18 to 80 years old who have to perform diagnostic tests such as magnetic resonance imaging tac ultrasound etc

Colors
0054AA
0677BA
7BADD7
CADEEF
E8F1F8
0094D4
00A9DD
6FCCEA
C7EBF8
E9F6FB
00AB8E
00BBA5
67D7C9
C6EFE9
E9F9F6

Requirements
Must have
• my project should be impactful and attractive. When the user sees my post he must be attracted
Nice to have
• I would like to highlight our diagnostic machines, so that the customers understand immediately what we are doing. As indicated on our website www.corvalux.it

```html
<!DOCTYPE html>
<html lang="en">
<head>
<meta charset="UTF-8">
<title>Corvalux – Healthcare Diagnostic Center</title>
<link rel="stylesheet" href="https://fonts.googleapis.com/css2?family=Poppins:wght@500;600;700;800&display=swap">
<style>
  :root{
    --navy:#0054AA;
    --blue:#0677BA;
    --sky:#7BADD7;
    --mist:#CADEEF;
    --ice:#E8F1F8;
    --headline-blue:#1D55A0;
    --teal:#00AB8E;
    --teal-deep:#008E76;
    --teal-light:#10B191;
    --white:#FFFFFF;
  }
  html,body{margin:0;padding:0;overflow:hidden;background:#fff;}
  .banner{
    position:relative;width:1200px;height:1200px;overflow:hidden;
    font-family:"Poppins",sans-serif;color:var(--white);
  }
  .machine-photo{
    position:absolute;inset:0 0 300px 0;
    background:
      radial-gradient(circle at 78% 30%, #dfe4ea 0 14%, #f4f6f8 15% 22%, #e6e9ed 23% 40%, transparent 55%),
      radial-gradient(ellipse at 35% 62%, #bfe0f5 0 18%, transparent 40%),
      linear-gradient(100deg,#f7f9fb 0%,#eef2f6 45%,#e3e8ee 100%);
  }
  .waves{position:absolute;inset:0;width:1200px;height:1200px;}
  .brand{
    position:absolute;left:58px;top:74px;display:flex;align-items:center;gap:16px;
  }
  .brand-dot{width:40px;height:40px;border-radius:50%;background:var(--teal);}
  .brand-name{font-size:70px;font-weight:700;color:var(--blue);line-height:1;letter-spacing:-1px;}
  .headline{
    position:absolute;left:80px;top:222px;margin:0;
    font-size:98px;font-weight:800;line-height:104px;letter-spacing:-1px;
  }
  .headline span{display:block;}
  .headline .line-blue{color:var(--headline-blue);}
  .headline .line-green{color:var(--teal-light);}
  .tagline{
    position:absolute;left:74px;top:898px;margin:0;
    font-size:35px;font-weight:700;line-height:44px;
  }
  .call-button{
    position:absolute;left:56px;top:1006px;width:481px;height:86px;
    border-radius:43px;background:var(--teal);display:flex;align-items:center;
  }
  .call-icon{
    width:64px;height:64px;border-radius:50%;background:var(--teal-deep);
    margin-left:11px;display:flex;align-items:center;justify-content:center;
  }
  .call-text{margin-left:14px;font-size:29px;font-weight:500;}
  .features{position:absolute;left:628px;top:930px;margin:0;padding:0;list-style:none;}
  .features li{display:flex;align-items:center;height:62px;font-size:29px;font-weight:500;}
  .features svg{margin-right:24px;}
  .contact-bar{
    position:absolute;left:39px;right:30px;top:1140px;
    display:flex;font-size:24px;font-weight:600;
  }
  .contact-bar .hours{width:302px;}
  .contact-bar .email{width:299px;}
</style>
</head>
<body>
<div class="banner">
  <div class="machine-photo" role="img" aria-label="Photo of a white MRI scanner with a light blue patient table in a bright clinic room"></div>

  <svg class="waves" viewBox="0 0 1200 1200" aria-hidden="true">
    <path d="M0,610 C250,560 460,720 720,690 C920,668 1060,600 1200,630 L1200,1200 L0,1200Z" fill="#CADEEF" opacity=".75"/>
    <path d="M0,690 C220,640 420,770 660,765 C900,760 1060,640 1200,650 L1200,1200 L0,1200Z" fill="#7BADD7" opacity=".85"/>
    <path d="M0,790 C260,730 470,840 720,845 C960,850 1090,760 1200,770 L1200,1200 L0,1200Z" fill="#0677BA" opacity=".85"/>
    <path d="M0,870 C220,850 420,890 720,880 C960,872 1100,855 1200,845 L1200,1200 L0,1200Z" fill="#0054AA"/>
  </svg>

  <div class="brand">
    <span class="brand-name">Corvalux</span>
    <span class="brand-dot"></span>
  </div>

  <h1 class="headline">
    <span class="line-blue">HEALTHCARE</span>
    <span class="line-green">DIAGNOSTIC</span>
    <span class="line-green">CENTER</span>
  </h1>

  <p class="tagline">PIONEERS IN<br>DIAGNOSTIC PRACTICE</p>

  <div class="call-button">
    <span class="call-icon">
      <svg width="30" height="30" viewBox="0 0 24 24" aria-hidden="true"><path fill="#fff" d="M6.6 10.8c1.4 2.8 3.8 5.1 6.6 6.6l2.2-2.2c.3-.3.7-.4 1-.2 1.1.4 2.3.6 3.6.6.6 0 1 .4 1 1V20c0 .6-.4 1-1 1C10.6 21 3 13.4 3 4c0-.6.4-1 1-1h3.5c.6 0 1 .4 1 1 0 1.3.2 2.5.6 3.6.1.3 0 .7-.2 1z"/></svg>
    </span>
    <span class="call-text">Call Us : +123-555-0147</span>
  </div>

  <ul class="features">
    <li><svg width="50" height="40" viewBox="0 0 50 40" aria-hidden="true"><circle cx="18" cy="20" r="18" fill="#00AB8E"/><path d="M8,20 L17,29 L44,4" stroke="#fff" stroke-width="6" fill="none" stroke-linecap="round" stroke-linejoin="round"/></svg>Special Modern Equipment</li>
    <li><svg width="50" height="40" viewBox="0 0 50 40" aria-hidden="true"><circle cx="18" cy="20" r="18" fill="#00AB8E"/><path d="M8,20 L17,29 L44,4" stroke="#fff" stroke-width="6" fill="none" stroke-linecap="round" stroke-linejoin="round"/></svg>We treat all people with care</li>
    <li><svg width="50" height="40" viewBox="0 0 50 40" aria-hidden="true"><circle cx="18" cy="20" r="18" fill="#00AB8E"/><path d="M8,20 L17,29 L44,4" stroke="#fff" stroke-width="6" fill="none" stroke-linecap="round" stroke-linejoin="round"/></svg>Best Experience</li>
  </ul>

  <div class="contact-bar">
    <span class="hours">Mon-Fri 8:00-19:00</span>
    <span class="email">info@corvalux.it</span>
    <span class="address">Collina Road, 17 47895, Borgo Alto, RSM</span>
  </div>
</div>
</body>
</html>
```